Tour agency for FIT and groups need a business card design

We need a business card design for a tour agency company that is based in Perth called" LUMEN QX", we aim to provide customise, unique and seamless travel arrangement for FIT and groups. We serve both high profile businessperson, government authorities, business partners, executives and investors. The name card should be more professional looking.

Target Market(s)

High profile businessperson, government authorities, business partners, executives and investors.

Industry/Entity Type

Tourism

Contact Information for Business Card

Lumen QX
Level 1, 218 Marbury Crescent, Tallowdale WA, 6015
www.lumenqx.com.au

Font styles to use
Serif

Colors

Designer to choose colors to be used in the design.

Requirements
Must have
• My project must have a company logo
Nice to have
• a more professional and solid yet friendly name card design. We may want to include chinese name in the name card as well. Edge of the card can be filled with gold and we think that transparent name cards are interesting.

```html
<!DOCTYPE html>
<html lang="en">
<head>
<meta charset="utf-8">
<title>Lumen QX — Business Card</title>
<link rel="stylesheet" href="https://fonts.googleapis.com/css2?family=Fira+Sans+Condensed:wght@300;400&display=swap">
<style>
  :root {
    --bg: #e4e4e6;
    --card-light: #ffffff;
    --card-dark: #050505;
    --ink: #2b2b2b;
    --ink-soft: #555555;
    --rule: #8a8a8a;
    --paper-white: #ffffff;
  }
  * { box-sizing: border-box; margin: 0; padding: 0; }
  html, body { width: 1200px; height: 1200px; overflow: hidden; }
  body {
    background: var(--bg);
    font-family: "Fira Sans Condensed", "Arial Narrow", sans-serif;
    position: relative;
  }
  .card {
    position: absolute;
    left: 180px;
    width: 840px;
    height: 480px;
    box-shadow: 0 6px 18px rgba(0,0,0,0.12);
  }
  .card-front { top: 90px; background: var(--card-light); color: var(--ink); }
  .card-back { top: 630px; background: var(--card-dark); }

  .contact { position: absolute; left: 64px; top: 62px; width: 440px; }
  .person-name { font-weight: 300; font-size: 36px; letter-spacing: 1px; color: var(--ink); }
  .person-title { font-weight: 300; font-size: 21px; color: var(--ink-soft); margin: 2px 0 14px; }
  .detail {
    display: flex; align-items: center; gap: 10px;
    font-weight: 300; font-size: 22px; color: var(--ink); margin-bottom: 10px;
  }
  .detail svg { width: 20px; height: 20px; flex: none; fill: var(--ink-soft); }
  .detail-address { padding-bottom: 12px; border-bottom: 1.5px solid var(--rule); font-size: 20px; white-space: nowrap; }

  .brand {
    position: absolute; display: flex; align-items: center; gap: 16px;
    font-weight: 400; letter-spacing: 2px;
  }
  .card-front .brand { right: 64px; bottom: 90px; font-size: 46px; color: var(--ink); }
  .card-back .brand { left: 50%; top: 50%; transform: translate(-50%, -50%); font-size: 52px; color: var(--paper-white); }
  .brand-dot { width: 34px; height: 34px; border-radius: 50%; background: currentColor; flex: none; }
</style>
</head>
<body>
  <section class="card card-front" aria-label="Card front">
    <div class="contact">
      <h1 class="person-name">ALEX MOREAU</h1>
      <p class="person-title">Director</p>
      <p class="detail">
        <svg viewBox="0 0 20 20" aria-hidden="true"><rect x="5" y="1" width="10" height="18" rx="2"/><rect x="7" y="3.5" width="6" height="9" fill="#fff"/></svg>
        123-555-0142
      </p>
      <p class="detail">
        <svg viewBox="0 0 20 20" aria-hidden="true"><circle cx="10" cy="10" r="8.5" fill="none" stroke="#555" stroke-width="1.5"/><ellipse cx="10" cy="10" rx="3.5" ry="8.5" fill="none" stroke="#555" stroke-width="1.3"/><path d="M2 10h16M3.5 6h13M3.5 14h13" stroke="#555" stroke-width="1.2"/></svg>
        www.lumenqx.com.au
      </p>
      <p class="detail">
        <svg viewBox="0 0 20 20" aria-hidden="true"><rect x="1" y="4" width="18" height="12"/><path d="M1.5 4.5 10 11l8.5-6.5" fill="none" stroke="#fff" stroke-width="1.4"/></svg>
        alex@lumenqx.com.au
      </p>
      <p class="detail detail-address">
        <svg viewBox="0 0 20 20" aria-hidden="true"><path d="M10 1a6 6 0 0 0-6 6c0 4.5 6 12 6 12s6-7.5 6-12a6 6 0 0 0-6-6zm0 8.5A2.5 2.5 0 1 1 10 4.5a2.5 2.5 0 0 1 0 5z"/></svg>
        Level 1, 218 Marbury Crescent, Tallowdale WA, 6015
      </p>
    </div>
    <div class="brand"><span class="brand-dot" aria-hidden="true"></span>LUMEN QX</div>
  </section>

  <section class="card card-back" aria-label="Card back">
    <div class="brand"><span class="brand-dot" aria-hidden="true"></span>LUMEN QX</div>
  </section>
</body>
</html>
```